Commercial janitorial company looking for a fresh and modern website design

We need a new website design for our Edmonton, Alberta-based commercial cleaning company called Brevick Custodial Limited. We have been providing services throughout Alberta for over 50 years, and have a strong customer-oriented service reputation. We are working to re-brand our image and the next crucial piece of that is an informative, simple, and modern website. We provide full service office and industrial cleaning, periodic services, and basic building maintenance, with a focus on being a 'silent partner' for our clients, allowing them to focus on their core business services. We are committed to the highest safety standards and industry best practices for productivity, employing environmentally friendly products practices in all our locations.

We would like a visually pleasing, easy-to-navigate website structure that provides clear communication through imagery and minimal text.

Target Market(s)

Commercial businesses

Industry/Entity Type

It Company

Font styles to use
Other font styles liked:
• Segoe (similar to our logo's font)

Requirements
Must have
• We would like the landing page to be extremely straightforward, with minimal scrolling required, and minimal text presence. We will likely have up to 5 sub-menus / pages, leading off from the main landing page. These pages will have further text on them, supplying further information. We would prefer their location on the top of the screen to be locked or in some way present during any page scrolling.
• Our logos are also available in eps, pdf, ai formats.
Nice to have
• Some websites that we like the presentation of include:
• tanglorn.hr
• quintbrook.com
• vox.com
• morvill.com
• tryplanko.com
• zunor.com

```html
<!DOCTYPE html>
<html lang="en">
<head>
<meta charset="utf-8">
<title>Brevick Custodial Limited — Commercial Cleaning</title>
<link rel="stylesheet" href="https://fonts.googleapis.com/css2?family=Raleway:wght@400;500&family=Open+Sans:ital,wght@0,400;0,600;1,400&family=Gochi+Hand&display=swap">
<style>
:root{
  --blue:#0f9ad9;
  --blue-soft:#3aa7e0;
  --green:#6cb644;
  --green-dark:#4a8f28;
  --ink:#3c3c3c;
  --grey:#777;
  --line:#cfcfcf;
  --light:#eeeeee;
  --footer:#585858;
  --white:#ffffff;
}
*{box-sizing:border-box;margin:0;padding:0}
html,body{width:1200px;height:2400px;overflow:hidden;background:var(--white)}
body{position:relative;font-family:"Open Sans",sans-serif;color:var(--ink)}
.abs{position:absolute}

/* header */
.site-header{position:absolute;left:0;top:0;width:1200px;height:110px;background:var(--white);border-bottom:1px solid #e4e4e4}
.brand{position:absolute;display:flex;align-items:center;gap:12px;font-family:"Raleway",sans-serif;font-weight:400;letter-spacing:1px}
.brand-mark{display:block;background:var(--blue)}
.site-header .brand{left:115px;top:34px;font-size:32px;color:#555}
.site-header .brand-mark{width:26px;height:26px}
.main-nav{position:absolute;top:48px;left:0;font-family:"Raleway",sans-serif;font-size:15px;color:#666}
.main-nav a{position:absolute;white-space:nowrap;color:inherit;text-decoration:none}
.main-nav a.is-current{color:var(--blue)}

/* hero */
.hero{position:absolute;left:0;top:110px;width:1200px;height:518px;overflow:hidden;
  background:linear-gradient(100deg,#d8d8d6 0%,#c9c7c3 30%,#b9c4cc 55%,#d5d9dc 100%)}
.hero-photo{position:absolute;inset:0}
.hero-title{position:absolute;left:130px;top:148px;font-family:"Gochi Hand",cursive;font-size:44px;letter-spacing:3px;color:var(--white);text-shadow:0 1px 3px rgba(0,0,0,.35)}
.hero-sub{position:absolute;left:132px;top:214px;font-family:"Gochi Hand",cursive;font-size:22px;letter-spacing:2px;color:var(--white);text-shadow:0 1px 3px rgba(0,0,0,.35)}
.hero-arrow{position:absolute;top:228px}
.quote-form{position:absolute;left:781px;top:84px;width:312px;height:344px;background:rgba(108,182,68,.93)}
.quote-form h2{position:absolute;left:29px;top:22px;font-family:"Raleway",sans-serif;font-weight:400;font-size:27px;color:var(--white)}
.field{position:absolute;left:29px;width:252px;height:29px;background:#f4f4f4;border:1px solid #dcdcdc;font-size:12px;color:#999;padding:6px 9px}
.field-message{height:80px}
.submit{position:absolute;left:27px;top:273px;width:254px;height:45px;background:var(--green-dark);color:var(--white);font-family:"Raleway",sans-serif;font-size:16px;letter-spacing:1px;text-align:center;line-height:45px}

/* welcome */
.welcome{position:absolute;left:0;top:628px;width:1200px;height:335px}
.notch{position:absolute;left:584px;top:-1px}
.welcome h1{position:absolute;left:104px;top:58px;font-family:"Raleway",sans-serif;font-weight:400;font-size:32px;color:var(--blue)}
.welcome h1 span{color:#555}
.welcome-copy{position:absolute;left:104px;top:114px;width:620px;font-size:13.5px;line-height:21px;color:var(--grey)}
.welcome-copy p{margin-bottom:10px}
.welcome-badge{position:absolute;left:784px;top:112px;width:220px;display:flex;align-items:center;gap:14px;font-family:"Raleway",sans-serif;font-size:34px;color:var(--blue);letter-spacing:2px}
.welcome-badge i{display:block;width:40px;height:40px;border-radius:50%;background:var(--green)}

/* features */
.feature{position:absolute;top:963px;width:600px;height:382px;color:var(--white)}
.feature-do{left:0;background:var(--green)}
.feature-are{left:600px;background:var(--blue)}
.feature h2{position:absolute;top:76px;font-weight:400;font-size:28px}
.feature-text{position:absolute;top:122px;width:290px;font-size:13px;line-height:21px}
.feature-text p{margin-bottom:13px}
.btn-outline{position:absolute;top:280px;width:120px;height:38px;border:2px solid var(--white);border-radius:20px;text-align:center;line-height:34px;font-size:14px}
.feature-icon{position:absolute;border-radius:12px;background:rgba(255,255,255,.18)}

/* operate */
.operate{position:absolute;left:0;top:1345px;width:1200px;height:485px}
.operate-mark{position:absolute;left:585px;top:14px;width:30px;height:30px;background:var(--blue)}
.section-rule{position:absolute;top:72px;height:1px;background:var(--line)}
.operate h2{position:absolute;left:0;width:1200px;top:56px;text-align:center;font-weight:400;font-size:22px;color:#333}
.place{position:absolute;top:113px;width:330px;text-align:center}
.place-photo{width:219px;height:219px;border-radius:50%;margin:0 auto}
.place h3{margin-top:33px;font-weight:400;font-size:22px;color:var(--green)}
.place p{margin-top:6px;font-size:13px;line-height:22px;color:#888}
.slider-arrow{position:absolute;top:208px}

/* testimonials */
.testimonials{position:absolute;left:0;top:1830px;width:1200px;height:330px;background:var(--light)}
.testimonials h2{position:absolute;width:1200px;top:40px;text-align:center;font-weight:400;font-size:29px;color:#222}
.quote-card{position:absolute;top:93px;height:151px;background:var(--blue);color:var(--white);font-style:italic;font-size:13.5px;line-height:21px;text-align:center;padding:22px 40px}
.quote-card.is-muted{color:rgba(255,255,255,.35)}
.avatar{position:absolute;top:205px;width:64px;height:64px;border-radius:50%;border:3px solid var(--white);background:linear-gradient(#d9b59a,#a57c62)}
.author{position:absolute;top:279px;width:300px;text-align:center;font-size:13px;color:#444}

/* footer */
.site-footer{position:absolute;left:0;top:2150px;width:1200px;height:250px}
.site-footer .brand{left:0;width:1200px;justify-content:center;top:52px;font-size:30px;color:var(--white)}
.site-footer .brand-mark{width:24px;height:24px;background:var(--white)}
.footer-nav{position:absolute;top:119px;width:1200px;text-align:center;font-size:14.5px;color:var(--white);word-spacing:2px}
.footer-nav span{margin:0 9px}
.legal{position:absolute;top:155px;width:1200px;text-align:center;font-size:11px;color:#ddd}
.social{position:absolute;top:188px;left:528px;display:flex;gap:4px}
.social i{display:block;width:32px;height:32px;border-radius:50%;background:var(--white)}
</style>
</head>
<body>

<header class="site-header">
  <div class="brand"><span class="brand-mark"></span>BREVICK</div>
  <nav class="main-nav">
    <a class="is-current" style="left:419px">Home</a>
    <a style="left:488px">What We Do</a>
    <a style="left:605px">Where We Operate</a>
    <a style="left:770px">Who We Are</a>
    <a style="left:883px">Work With Us</a>
    <a style="left:1010px">Contact Us</a>
  </nav>
</header>

<section class="hero">
  <div class="hero-photo" role="img" aria-label="Photo of three smiling cleaning staff in blue aprons standing in a bright office beside a vacuum cleaner and a wet floor sign"></div>
  <div class="hero-title">COMMERCIAL CLEANING</div>
  <div class="hero-sub">CRAS ANTE VITAE ENIM IACULIS ALIQU</div>
  <svg class="hero-arrow" style="left:6px" width="18" height="30" viewBox="0 0 18 30"><path d="M15 3 3 15l12 12" fill="none" stroke="#fff" stroke-width="3"/></svg>
  <svg class="hero-arrow" style="left:1176px" width="18" height="30" viewBox="0 0 18 30"><path d="M3 3l12 12L3 27" fill="none" stroke="#fff" stroke-width="3"/></svg>
  <form class="quote-form">
    <h2>GET A QUOTE</h2>
    <div class="field" style="top:67px">Name</div>
    <div class="field" style="top:105px">Email address</div>
    <div class="field" style="top:145px">Phone</div>
    <div class="field field-message" style="top:184px">Message</div>
    <div class="submit">SUBMIT</div>
  </form>
</section>

<section class="welcome">
  <svg class="notch" width="32" height="16" viewBox="0 0 32 16"><path d="M0 0h32L16 16z" fill="#c9c7c3"/></svg>
  <h1>WELCOME TO <span>BREVICK</span></h1>
  <div class="welcome-copy">
    <p>Since 1963 Brevick Custodial Limited has been providing commercial cleaning services to clients across Alberta. Brevick has a philosophy that relationships are the key to success and we devote many &nbsp;man hours to developing quality teams.</p>
    <p>These teams are well versed in maintaining relationships with &nbsp;clients as well as understanding our comprehensive quality assurance and safety programs. As a result, &nbsp;we have become the choice service provider for our clients and employees.</p>
  </div>
  <div class="welcome-badge"><i></i>BREVICK</div>
</section>

<section class="feature feature-do">
  <h2 style="left:115px">What We Do</h2>
  <div class="feature-text" style="left:115px">
    <p>As a full-spectrum janitorial services company, we employ a team-focused, ‘all hands on deck’ approach, wherein every team member is empowered to address client concerns.</p>
    <p>This allows us to be very flexible and responsive to client needs.</p>
  </div>
  <div class="btn-outline" style="left:112px">Read More</div>
  <div class="feature-icon" style="left:408px;top:85px;width:168px;height:160px" role="img" aria-label="White line illustration of a canister vacuum cleaner"></div>
</section>

<section class="feature feature-are">
  <h2 style="left:56px">Who We Are</h2>
  <div class="feature-text" style="left:56px">
    <p>Objective: &nbsp;Brevick has a standing motto of ‘We want to be your silent partner’.</p>
    <p>To this end, our overriding goal is to provide service in a matter that allows our clients to focus solely on their core business activities.</p>
  </div>
  <div class="btn-outline" style="left:52px">Read More</div>
  <div class="feature-icon" style="left:320px;top:77px;width:152px;height:192px" role="img" aria-label="White line illustration of a broom with soap bubbles"></div>
</section>

<section class="operate">
  <div class="operate-mark"></div>
  <div class="section-rule" style="left:106px;width:366px"></div>
  <div class="section-rule" style="left:706px;width:372px"></div>
  <h2>Where We Operate</h2>
  <svg class="slider-arrow" style="left:105px" width="18" height="34" viewBox="0 0 18 34"><path d="M15 3 3 17l12 14" fill="none" stroke="#bbb" stroke-width="3"/></svg>
  <svg class="slider-arrow" style="left:1075px" width="18" height="34" viewBox="0 0 18 34"><path d="M3 3l12 14L3 31" fill="none" stroke="#bbb" stroke-width="3"/></svg>
  <div class="place" style="left:102px">
    <div class="place-photo" role="img" aria-label="Photo of a worker cleaning an office computer screen" style="background:linear-gradient(135deg,#e6e6e6,#8a93a6 55%,#3b4a7a)"></div>
    <h3>Office facilities</h3>
    <p>massa est sed nisl Class aptent taciti sociosqu<br>ad litora torquent per conubia nostra per</p>
  </div>
  <div class="place" style="left:433px">
    <div class="place-photo" role="img" aria-label="Photo of a chef in white uniform in a commercial kitchen" style="background:linear-gradient(135deg,#c9c2b8,#7a4a3a 55%,#e8e4de)"></div>
    <h3>Retail facilities</h3>
    <p>massa est sed nisl Class aptent taciti sociosqu<br>ad litora torquent per conubia nostra per</p>
  </div>
  <div class="place" style="left:765px">
    <div class="place-photo" role="img" aria-label="Photo of a worker mopping a large industrial floor" style="background:linear-gradient(160deg,#5a5f66,#9aa0a6 50%,#c4c8cc)"></div>
    <h3>Industrial facilities</h3>
    <p>massa est sed nisl Class aptent taciti sociosqu<br>ad litora torquent per conubia nostra per</p>
  </div>
</section>

<section class="testimonials">
  <h2>Testimonials</h2>
  <div class="quote-card" style="left:179px;width:379px">Morbi ornare gravida elit Integer congue augue et malesuada iaculis ipsum dui aliquet felis at cursus magna nisl nec elit Praesent elementum elit at tellus nec ultricies sit amet porttitor matt</div>
  <div class="avatar" role="img" aria-label="Portrait photo of the reviewer" style="left:342px"></div>
  <div class="author" style="left:222px">By Author Name, City Location</div>
  <div class="quote-card is-muted" style="left:606px;width:388px">Morbi ornare gravida elit Integer congue augue et malesuada iaculis ipsum dui aliquet felis at cursus magna nisl nec elit Praesent elementum elit at tellus nec ultricies sit amet porttitor matt</div>
  <div class="avatar" role="img" aria-label="Portrait photo of the reviewer" style="left:768px"></div>
  <div class="author" style="left:644px">By Author Name, City Location</div>
</section>

<footer class="site-footer">
  <svg class="abs" style="left:0;top:0" width="1200" height="250" viewBox="0 0 1200 250">
    <path d="M0 44 L590 2 L1200 58 V250 H0Z" fill="#585858"/>
    <path d="M0 44 L590 2 L590 10 L0 58Z" fill="#0f9ad9"/>
    <path d="M590 2 L1200 48 L1200 62 L590 10Z" fill="#6cb644"/>
  </svg>
  <div class="brand"><span class="brand-mark"></span>BREVICK</div>
  <div class="footer-nav"><span>HOME</span><span>WHAT WE DO</span><span>WHERE WE OPERATE</span><span>WHO WE ARE</span><span>WORK WITH US</span><span>CONTACT US</span></div>
  <div class="legal">© 2016 Company Name &nbsp;All right reserved &nbsp;Term of Use</div>
  <div class="social"><i></i><i></i><i></i><i></i></div>
</footer>

</body>
</html>
```